Finally a Vodka produced for women ! (Label Design)

We are a small distillery based in Melbourne, Australia and we need a Vodka label design solution that will appeal to women aged 30-50 years and radiate luxury. Full Details are in a design brief attached. We thank you in advance.

Target Market(s)

Affluent females 30-50 years.

Industry/Entity Type

Spirits/Alcohol

Requirements
Must have
• Be clear this is a luxury Vodka.
Nice to have
• Elegance.

```html
<!DOCTYPE html>
<html lang="en">
<head>
<meta charset="utf-8">
<title>Silver Wren Distillery – Premium Vodka Label</title>
<link rel="stylesheet" href="https://fonts.googleapis.com/css2?family=Bodoni+Moda:wght@700&family=Cinzel:wght@600;700&family=Pinyon+Script&family=Marcellus&display=swap">
<style>
  :root {
    --paper: #ffffff;
    --label: #fdfdfd;
    --ink: #0b0b0b;
    --gold: #f3d98f;
    --cream: #fff4d6;
    --white: #ffffff;
    --pink-soft: #f6b3c6;
    --pink: #ee7fa0;
    --rose: #e8466f;
    --red: #e4112f;
  }
  html, body {
    margin: 0;
    padding: 0;
    width: 1200px;
    height: 1200px;
    overflow: hidden;
    background: var(--paper);
  }
  .canvas {
    position: relative;
    width: 1200px;
    height: 1200px;
    overflow: hidden;
    background: var(--paper);
  }
  .label-sheet {
    position: absolute;
    left: 300px;
    top: 160px;
    width: 640px;
    height: 980px;
    background: var(--label);
    transform: rotate(4deg);
  }
  .ink-cloud {
    position: absolute;
    left: 320px;
    top: 180px;
    width: 560px;
    height: 940px;
  }
  .brand {
    position: absolute;
    left: 0;
    width: 1200px;
    top: 200px;
    text-align: center;
    font-family: "Marcellus", serif;
    color: var(--ink);
    padding-left: 12px;
    box-sizing: border-box;
  }
  .brand-name {
    margin: 0;
    font-size: 78px;
    line-height: 84px;
    letter-spacing: 4px;
    font-weight: 400;
  }
  .brand-sub {
    margin: 10px 0 0;
    font-size: 16px;
    letter-spacing: 11px;
    font-weight: 400;
  }
  .product {
    position: absolute;
    left: 0;
    width: 1200px;
    top: 572px;
    margin: 0;
    text-align: center;
    font-family: "Bodoni Moda", serif;
    font-weight: 700;
    font-size: 212px;
    line-height: 200px;
    letter-spacing: -2px;
    color: var(--ink);
    padding-left: 8px;
    box-sizing: border-box;
    -webkit-text-stroke: 1px var(--cream);
  }
  .grade {
    position: absolute;
    left: 0;
    width: 1200px;
    top: 738px;
    margin: 0;
    text-align: center;
    font-family: "Pinyon Script", cursive;
    font-size: 84px;
    line-height: 100px;
    color: var(--cream);
    -webkit-text-stroke: 1px #c9a24a;
    padding-right: 18px;
    box-sizing: border-box;
  }
  .rule {
    position: absolute;
    left: 464px;
    width: 270px;
    height: 1px;
    background: var(--gold);
  }
  .rule--upper { top: 838px; }
  .rule--lower { top: 1002px; }
  .variant {
    position: absolute;
    left: 0;
    width: 1200px;
    top: 854px;
    margin: 0;
    text-align: center;
    font-family: "Cinzel", serif;
    font-weight: 700;
    color: var(--ink);
    font-size: 60px;
    line-height: 68px;
    padding-right: 6px;
    box-sizing: border-box;
  }
  .variant span { display: block; }
  .details {
    position: absolute;
    left: 0;
    width: 1200px;
    top: 1018px;
    text-align: center;
    font-family: "Marcellus", serif;
    padding-right: 10px;
    box-sizing: border-box;
  }
  .details p { margin: 0; letter-spacing: 2px; }
  .origin { color: var(--white); font-size: 23px; line-height: 30px; }
  .strength, .volume { color: var(--gold); font-size: 19px; line-height: 28px; }
</style>
</head>
<body>
<main class="canvas">
  <div class="label-sheet"></div>

  <svg class="ink-cloud" viewBox="0 0 560 940" role="img" aria-label="Pink and red ink clouds swirling through water">
    <defs>
      <radialGradient id="cloud-core" cx="50%" cy="58%" r="55%">
        <stop offset="0%" stop-color="#e4112f"/>
        <stop offset="35%" stop-color="#e8466f"/>
        <stop offset="70%" stop-color="#f39ab3" stop-opacity="0.85"/>
        <stop offset="100%" stop-color="#f6b3c6" stop-opacity="0"/>
      </radialGradient>
      <linearGradient id="cloud-plume" x1="0" y1="0" x2="0" y2="1">
        <stop offset="0%" stop-color="#f6b3c6" stop-opacity="0"/>
        <stop offset="40%" stop-color="#f6b3c6" stop-opacity="0.7"/>
        <stop offset="100%" stop-color="#ee7fa0" stop-opacity="0.9"/>
      </linearGradient>
    </defs>
    <path d="M250 20 C330 80 300 200 380 280 C440 340 500 330 470 430 L90 430 C60 330 160 300 170 220 C180 120 220 80 250 20 Z" fill="url(#cloud-plume)"/>
    <ellipse cx="290" cy="560" rx="280" ry="300" fill="url(#cloud-core)"/>
    <ellipse cx="310" cy="860" rx="230" ry="80" fill="#ee7fa0" opacity="0.85"/>
  </svg>

  <header class="brand">
    <h1 class="brand-name">SILVER<br>WREN</h1>
    <p class="brand-sub">DISTILLERY</p>
  </header>

  <h2 class="product">VODKA</h2>
  <p class="grade">Premium</p>

  <div class="rule rule--upper"></div>
  <h3 class="variant"><span>ROSE QUARTZ</span><span>FILTERED</span></h3>
  <div class="rule rule--lower"></div>

  <section class="details">
    <p class="origin">100% AUSTRALIAN</p>
    <p class="strength">40%ALC/VOL</p>
    <p class="volume">700ML</p>
  </section>
</main>
</body>
</html>
```